A home-based beauty salon needs a website

Creation of an aesthetically pleasing and user-friendly website, crucial for showcasing our products, services and driving customer engagement/online bookings.

Focusing on key elements:
- mobile compatibility (fast loading on mobile)
- accessibility
- well-planned information architecture
- effective navigation
- simple forms (Contact Us)
- blog
- online store (e.g. shopify) to sell beauty products
- newsletter subscription
- online booking: integrate with existing engine = Fresha
- easy ongoing maintenance

Objective of website:
- Build online brand presence: classy, aesthetic and professional
- Drive online bookings
- Drive online sales

Services offered:
- Laser Hair Removal
- Chemical Peels
- Advanced Skin Treatments
- LED Light Therapy
- Teeth Whitening

Inspiration:
Ideal layout and function: https://velinorskin.ca/
Innovative and sleek design: https://www.studiotavi.sk/

Instagram: https://www.pictogrove.com/bramelskin_official/

Colour preferences: Black, White, and if possible Tropical Rainforest Palm Leave greens to match our feature-wall in the clinic room (see uploaded files for example behind our business logo). Open to seeing light pastel colours as well.

Copy: to be provided post design-phase
Images: of the clinic and our machines can be provided during design-phase
Font style: fancy and light to match the logo

Sections:
Home, About, Spa (Hydro-dermabrasion, LED Light Therapy, Peels, Facials, Signature Packages), Medical (Laser Hair Removal, Chemical Peels, Teeth Whitening), Contact, Blog

Industry/Entity Type

Beauty and Skincare Industry

Coding

Coded - Design and coding required

Number of Pages Required

5+ page

Colors

Designer to choose colors to be used in the design.

Requirements
Must have
• Integration with Shopify or similar, Integration with Afterpay or Zip Pay, Newsletter subscription pop-up or similar, Map to visualise location and make it easy for customers to find us, Integration with our Fresha booking engine, Integration with Instagram or Gallery under each service offering to present before vs after images of treatments to support the Consideration process
Nice to have
• (1) Contact Us Page: form + visual navigation of how to get to the clinic to make it easy to find us. (2) Online Store integration with Shopify. (3) Integrate Gallery or select Instagram pictures that match the service offered to help customers see potential results when selecting services. e.g. Teeth Whitening before and after on the Teeth Whitening service page. (4) Integrate Zip Pay or Afterpay next to product/service offers making it easy to understand potential repayments . (5)

```html
<!DOCTYPE html>
<html lang="en">
<head>
<meta charset="UTF-8">
<title>Glowing Skin</title>
<link href="https://fonts.googleapis.com/css2?family=Cormorant+Garamond:wght@400;700&family=Inter:wght@400&display=swap" rel="stylesheet">
<style>
  :root {
    --white: #ffffff;
    --ink: #111111;
    --body-text: #2b2b2b;
    --palm-green: #3b6c4d;
    --button-black: #0b0b0b;
    --skin-light: #f0d3bf;
    --skin-mid: #d9ad8f;
    --skin-deep: #b98366;
  }
  * { margin: 0; padding: 0; box-sizing: border-box; }
  html, body {
    width: 1200px;
    height: 2473px;
    overflow: hidden;
    background: var(--white);
  }
  .hero {
    position: relative;
    width: 1200px;
    height: 2473px;
  }
  .hero-portrait {
    position: absolute;
    left: 100px;
    top: -5px;
    width: 950px;
    height: 950px;
    border-radius: 50%;
    background: radial-gradient(circle at 45% 40%, var(--skin-light) 0%, var(--skin-mid) 60%, var(--skin-deep) 100%);
  }
  .hero-title {
    position: absolute;
    top: 1055px;
    left: 0;
    width: 1200px;
    text-align: center;
    font-family: 'Cormorant Garamond', serif;
    color: var(--ink);
    line-height: 143px;
  }
  .hero-title .light {
    display: block;
    font-weight: 400;
    font-size: 124px;
    letter-spacing: -2px;
  }
  .hero-title .bold {
    display: block;
    font-weight: 700;
    font-size: 124px;
    letter-spacing: -1px;
  }
  .hero-copy {
    position: absolute;
    top: 1415px;
    left: 50px;
    width: 1100px;
    text-align: center;
    font-family: 'Inter', sans-serif;
    font-size: 50px;
    line-height: 97px;
    color: var(--body-text);
  }
  .cta-bar {
    position: absolute;
    left: 0;
    top: 2190px;
    width: 1200px;
    height: 283px;
    background: var(--palm-green);
  }
  .cta-button {
    position: absolute;
    top: 50px;
    width: 527px;
    height: 173px;
    display: flex;
    align-items: center;
    justify-content: center;
    gap: 18px;
    font-family: 'Inter', sans-serif;
    font-size: 47px;
    letter-spacing: 6px;
    color: var(--white);
    text-decoration: none;
  }
  .cta-button svg { width: 50px; height: 50px; }
  .cta-book { left: 57px; background: var(--button-black); }
  .cta-call { left: 617px; border: 4px solid var(--white); }
</style>
</head>
<body>
<main class="hero">
  <div class="hero-portrait" role="img" aria-label="Portrait of a woman with radiant, glowing skin"></div>
  <h1 class="hero-title">
    <span class="light">Are you Ready for</span>
    <span class="bold">Glowing Skin?</span>
  </h1>
  <p class="hero-copy">Lorem ipsum dolor sit amet, consectetur adipiscing elit. Integer et lorem non odio aliquet sagittis. Pellentesque eu risus ut leo scelerisque sodales at quis est. Fusce at erat accumsan, ultrices nisl eu, feugiat libero. Fusce id tincidunt quam. Lorem ipsum dolor sit amet, consectetur.</p>
  <div class="cta-bar">
    <a class="cta-button cta-book" href="#book">BOOK NOW
      <svg viewBox="0 0 24 24" fill="none" stroke="currentColor" stroke-width="2"><path d="M3 12h17M13 5l7 7-7 7"/></svg>
    </a>
    <a class="cta-button cta-call" href="#call">CALL US
      <svg viewBox="0 0 24 24" fill="none" stroke="currentColor" stroke-width="2"><path d="M3 12h17M13 5l7 7-7 7"/></svg>
    </a>
  </div>
</main>
</body>
</html>
```